we need a business card as well as a logo that can be used for signs etc.
this is a very formal, classy , elegant function centre, as well as café. I am after a design that stands out and grabs people attentions. my colours theme is really warm ,colours like chocolate browns, and latte type colours with really deep red tones
not bright red, just warm tones. this is a place that very wealthy and maybe even celebs will come so I need it to be appealing.
Industry/Entity Type
Business
Contact Information for Business Card
Blue Fern
café and function centre @ hallam orchard.
wedding and function specialists,
Barrow parkway, lucknow,ph 0438157240

```html
<!DOCTYPE html>
<html lang="en">
<head>
<meta charset="utf-8">
<title>Blue Fern Café &amp; Function Centre – Business Card</title>
<link href="https://fonts.googleapis.com/css2?family=Lancelot&family=Dosis:wght@500&family=Quicksand:wght@500&display=swap" rel="stylesheet">
<style>
  :root {
    --backdrop: #6f6f6f;
    --chocolate: #55281b;
    --cream: #ffffff;
    --flourish: #f3ebe7;
    --ink: #4a2016;
  }
  * { margin: 0; padding: 0; box-sizing: border-box; }
  html, body {
    width: 1200px;
    height: 1000px;
    overflow: hidden;
    background: var(--backdrop);
  }
  .business-card {
    position: absolute;
    left: 180px;
    top: 237px;
    width: 840px;
    height: 525px;
    background: var(--cream);
    box-shadow: 0 2px 6px rgba(0,0,0,0.35);
    overflow: hidden;
  }
  .card-face {
    position: absolute;
    left: 0; top: 0;
    width: 840px;
    height: 448px;
    background: var(--chocolate);
    color: var(--cream);
  }
  .venue-name {
    position: absolute;
    left: 449px;
    top: 30px;
    font-family: "Lancelot", serif;
    font-size: 46px;
    line-height: 1;
    white-space: nowrap;
  }
  .venue-tagline {
    position: absolute;
    left: 451px;
    top: 92px;
    font-family: "Dosis", sans-serif;
    font-weight: 500;
    font-size: 20px;
    white-space: nowrap;
  }
  .flourish {
    position: absolute;
    left: 290px;
    width: 260px;
    height: 62px;
    display: block;
  }
  .flourish-top { top: 218px; }
  .flourish-bottom { top: 352px; }
  .business-name {
    position: absolute;
    left: 0;
    width: 840px;
    top: 287px;
    text-align: center;
    font-family: "Lancelot", serif;
    font-size: 50px;
    line-height: 1;
    white-space: nowrap;
  }
  .contact-band {
    position: absolute;
    left: 0;
    top: 448px;
    width: 840px;
    height: 77px;
    display: flex;
    align-items: center;
    justify-content: center;
    gap: 26px;
    font-family: "Quicksand", sans-serif;
    font-weight: 500;
    font-size: 24px;
    color: var(--ink);
  }
  .contact-phone {
    display: flex;
    align-items: center;
    gap: 8px;
  }
  .phone-icon { width: 16px; height: 20px; }
</style>
</head>
<body>
  <div class="business-card">
    <div class="card-face">
      <div class="venue-name">Hallam Orchard</div>
      <div class="venue-tagline">Wedding &amp; Function Specialists</div>

      <svg class="flourish flourish-top" viewBox="0 0 260 62" role="img" aria-label="Ornamental scroll flourish above the name">
        <rect x="0" y="0" width="260" height="62" rx="20" fill="var(--flourish)" opacity="0.85"/>
      </svg>

      <div class="business-name">Blue Fern Café &amp; Function Centre</div>

      <svg class="flourish flourish-bottom" viewBox="0 0 260 62" role="img" aria-label="Ornamental scroll flourish below the name">
        <rect x="0" y="0" width="260" height="62" rx="20" fill="var(--flourish)" opacity="0.85"/>
      </svg>
    </div>

    <div class="contact-band">
      <span class="contact-address">Barrow Parkway, Ashworth</span>
      <span class="contact-phone">
        <svg class="phone-icon" viewBox="0 0 16 20" aria-hidden="true">
          <path d="M5 1 L8 1 L9 6 L6.5 7.5 Q7 12 10 14.5 L12.5 13 L15 17 L12 19 Q3 16 2.5 6 Q2.5 2 5 1 Z" fill="var(--ink)"/>
        </svg>
        0438157240
      </span>
    </div>
  </div>
</body>
</html>
```